Business Card for Makeup Artist

I need a business card designed for my makeup and hair artistry business which is primarily events and weddings focused. The card needs to be sleek, simple, stylish and appealing to women. I would prefer a white background but open to suggestions also. I also love the marble background look. I have attached some example pics. It needs to be a double sided card with logo and/or design on one side and contact details in the centre of the card on the other side. NO LOGO ON BACK. Examples attached.

Target Market(s)

Females age 14-55

Industry/Entity Type

Business

Contact Information for Business Card

Nora Pelling
Principal Makeup Artist
P: 0412 903 251
E: nora@lumivamakeup.com.au
W: www.lumivamakeup.com.au

Requirements
Should not have
• No yellow, green, red or blue in the design.

```html
<!DOCTYPE html>
<html lang="en">
<head>
<meta charset="utf-8">
<title>Lumiva Makeup Artistry – Business Card</title>
<link rel="stylesheet" href="https://fonts.googleapis.com/css2?family=Open+Sans:wght@400;600;700&display=swap">
<style>
  :root {
    --backdrop: #ece7e1;
    --card-gold-light: #d6a87a;
    --card-gold: #c49366;
    --card-gold-deep: #a97a51;
    --ink: #141110;
    --card-shadow: rgba(60, 40, 20, 0.22);
  }
  * { margin: 0; padding: 0; box-sizing: border-box; }
  html, body {
    width: 1200px;
    height: 900px;
    overflow: hidden;
    background: var(--backdrop);
    font-family: "Open Sans", Arial, sans-serif;
    color: var(--ink);
  }
  .stage {
    position: relative;
    width: 1200px;
    height: 900px;
  }
  .card {
    position: absolute;
    width: 540px;
    height: 330px;
    border-radius: 3px;
    background:
      radial-gradient(ellipse at 30% 20%, var(--card-gold-light) 0%, transparent 60%),
      linear-gradient(135deg, var(--card-gold) 0%, var(--card-gold-light) 45%, var(--card-gold-deep) 100%);
    box-shadow: 0 14px 34px var(--card-shadow);
  }
  .card--front { left: 90px; top: 110px; }
  .card--back  {
    left: 570px;
    top: 460px;
    display: flex;
    align-items: center;
    justify-content: center;
  }

  .brand {
    position: absolute;
    left: 150px;
    top: 110px;
    font-weight: 400;
    color: var(--ink);
    line-height: 1;
  }
  .brand__name {
    display: block;
    font-size: 58px;
    letter-spacing: 1px;
  }
  .brand__tagline {
    display: block;
    font-size: 17px;
    letter-spacing: 1.5px;
    margin-top: 6px;
    padding-left: 40px;
  }

  .contact {
    text-align: center;
    font-size: 14px;
    line-height: 1.5;
  }
  .contact__name {
    font-weight: 700;
    font-size: 19px;
  }
  .contact__role {
    font-size: 13px;
    margin-bottom: 18px;
  }
  .contact__list { list-style: none; }
  .contact__list li { margin-bottom: 4px; }
  .contact__label { font-weight: 700; }
</style>
</head>
<body>
<main class="stage">
  <section class="card card--front" aria-label="Card front">
    <div class="brand">
      <span class="brand__name">Lumiva</span>
      <span class="brand__tagline">MAKEUP ARTISTRY</span>
    </div>
  </section>

  <section class="card card--back" aria-label="Card back">
    <div class="contact">
      <p class="contact__name">Nora Pelling</p>
      <p class="contact__role">Principal Makeup Artist</p>
      <ul class="contact__list">
        <li><span class="contact__label">P:</span> 0412 903 251</li>
        <li><span class="contact__label">E:</span> nora@lumivamakeup.com.au</li>
        <li><span class="contact__label">W:</span> www.lumivamakeup.com.au</li>
      </ul>
    </div>
  </section>
</main>
</body>
</html>
```